PowerPoint presentation for new Building Certification business

We are Harbourline Compliance Group.

We are a young company providing a modern service in an industry that was predominately provided by inefficient local Council's who did not complete with anyone for work.

We are after a PowerPoint slide for presentations we hope to give prospective clients. The title page is to include a flash design that draws attention to our logo.

We also require an additional page for the body of the presentation. This is to be modern and simplistic but clearly recognisable with our brand and logo.

Target Market(s)

Architects. Draftsman. Developers. Project managers. Builders. Home owners.

Industry/Entity Type

Industry

Requirements
Must have
• Corporate logo and colours.
• Flash design to title page that involves our logo

```html
<!DOCTYPE html>
<html lang="en">
<head>
<meta charset="utf-8">
<title>Harbourline Compliance Group — Title Slide</title>
<link rel="stylesheet" href="https://fonts.googleapis.com/css2?family=Oswald:wght@600;700&family=Tinos&display=swap">
<style>
  :root {
    --sky: #d6ddf9;
    --sky-light: #e4e9fc;
    --sky-deep: #b9c5ef;
    --band: #e6ebfc;
    --rule: #5b6fc7;
    --navy: #1f2f8f;
    --brand: #3a4aa6;
    --brand-soft: #4f62bd;
    --body-text: #1e1e2a;
    --photo-frame: #5a72d0;
    --photo-warm: #f3b42a;
    --photo-cool: #9fb6e6;
  }
  * { margin: 0; padding: 0; box-sizing: border-box; }
  html, body { width: 1200px; height: 900px; overflow: hidden; }
  body { position: relative; background: var(--sky); }

  .slide { position: relative; width: 1200px; height: 900px; overflow: hidden; }

  .plan-backdrop {
    position: absolute; left: 0; width: 1200px;
  }
  .plan-backdrop--top {
    top: 0; height: 265px;
    background:
      radial-gradient(ellipse 420px 200px at 180px 60px, var(--sky-light) 0%, transparent 70%),
      radial-gradient(ellipse 380px 220px at 1000px 120px, var(--sky-deep) 0%, transparent 75%),
      radial-gradient(ellipse 300px 160px at 560px 200px, #c8d2f4 0%, transparent 75%),
      linear-gradient(170deg, var(--sky-light) 0%, var(--sky) 50%, #c6d0f3 100%);
  }
  .plan-backdrop--bottom {
    top: 690px; height: 210px;
    background:
      radial-gradient(ellipse 360px 180px at 240px 120px, #c4cef3 0%, transparent 75%),
      radial-gradient(ellipse 420px 200px at 960px 160px, var(--sky-deep) 0%, transparent 75%),
      radial-gradient(ellipse 300px 140px at 640px 40px, var(--sky-light) 0%, transparent 70%),
      linear-gradient(10deg, #c6d0f3 0%, var(--sky) 55%, var(--sky-light) 100%);
  }

  .feature-band {
    position: absolute; left: 0; top: 265px; width: 1200px; height: 425px;
    background: linear-gradient(90deg, #dde3fa 0%, var(--band) 40%, var(--band) 100%);
    border-top: 3px solid var(--rule);
    border-bottom: 3px solid var(--rule);
  }

  .brand-block {
    position: absolute; left: 92px; top: 296px; width: 476px;
    display: flex; flex-direction: column; align-items: center; gap: 20px;
  }
  .brand-square { width: 100px; height: 100px; background: var(--brand-soft); }
  .brand-name {
    width: 340px; text-align: center;
    font-family: "Oswald", sans-serif; font-weight: 600;
    font-size: 34px; line-height: 38px; letter-spacing: 2px;
    color: var(--brand); text-transform: uppercase;
  }

  .project-title {
    position: absolute; left: 92px; top: 514px; width: 476px;
    text-align: center;
    font-family: "Oswald", sans-serif; font-weight: 700;
    font-size: 50px; line-height: 1; letter-spacing: 1px;
    color: var(--navy); text-transform: uppercase;
  }

  .project-summary {
    position: absolute; left: 82px; top: 580px; width: 496px;
    text-align: center;
    font-family: "Tinos", serif; font-size: 21px; line-height: 34px;
    color: var(--body-text);
  }

  .project-photo {
    position: absolute; left: 640px; top: 318px; width: 487px; height: 324px;
    border: 5px solid var(--photo-frame);
    background: linear-gradient(135deg, var(--photo-warm) 0%, #f6d36a 35%, var(--photo-cool) 65%, #dfe6f6 100%);
  }

  .next-arrow { position: absolute; left: 1136px; top: 455px; width: 44px; height: 44px; }
</style>
</head>
<body>
<main class="slide">
  <div class="plan-backdrop plan-backdrop--top" role="img" aria-label="Faint blue architectural floor plan drawings across the top of the slide"></div>
  <div class="plan-backdrop plan-backdrop--bottom" role="img" aria-label="Faint blue architectural floor plan drawings across the bottom of the slide"></div>

  <section class="feature-band"></section>

  <div class="brand-block">
    <span class="brand-square"></span>
    <span class="brand-name">Harbourline Compliance Group</span>
  </div>

  <h1 class="project-title">Project Title Here</h1>
  <p class="project-summary">Lorem ipsum dolor sit ispum Lorem ipsum dolor<br>sit ispum Lorem ipsum dolor sit ispum</p>

  <div class="project-photo" role="img" aria-label="Photo of a yellow hard hat, drafting compass and protractor resting on building plans"></div>

  <svg class="next-arrow" viewBox="0 0 44 44" aria-label="Next slide">
    <circle cx="22" cy="22" r="19" fill="#eef1fd" stroke="#3f55b8" stroke-width="2.5"/>
    <path d="M17 13 L27 22 L17 31 Z" fill="#3f55b8"/>
  </svg>
</main>
</body>
</html>
```